Animal Puzzle game Needs Design

Need a redesign of the UI of this puzzle game and a forest background. This game is for any age. The design needs to be on separate layers in Photoshop. The design needs to be colorful and easy to see the different UI parts, sound control, progress bar, number of lives and number of moves.

Target Market(s)

All ages

Requirements
Must have
• Needs to have each of the UI elements and a background.

```html
<!DOCTYPE html>
<html lang="en">
<head>
<meta charset="utf-8">
<title>Puzzle Game – Level 1</title>
<link href="https://fonts.googleapis.com/css2?family=Open+Sans:wght@600;700;800&family=Arimo:wght@400;700&display=swap" rel="stylesheet">
<style>
  :root {
    --forest-dark: #1c3a14;
    --forest-mid: #3f7a25;
    --forest-light: #8cc23c;
    --text-white: #ffffff;
    --heart-red: #e8121e;
    --heart-number: #fff200;
    --level-fill: #6a0020;
    --level-ring: #f08a9a;
    --moves-yellow: #ffff00;
    --tile-red: #ff0000;
    --tile-yellow: #f5e800;
    --tile-blue: #2288ff;
    --tile-green: #55ff00;
    --bar-track: #2e3246;
    --bar-fill-top: #f0a818;
    --bar-fill-bottom: #d85a08;
  }
  * { margin: 0; padding: 0; box-sizing: border-box; }
  html, body { width: 1200px; height: 900px; overflow: hidden; }
  body { font-family: "Open Sans", sans-serif; color: var(--text-white); }
  .game-screen { position: relative; width: 1200px; height: 900px; overflow: hidden; }
  .forest-background {
    position: absolute; inset: 0;
    background:
      radial-gradient(ellipse at 55% 20%, rgba(200,230,120,0.55), transparent 55%),
      radial-gradient(ellipse at 85% 35%, rgba(140,200,60,0.5), transparent 50%),
      radial-gradient(ellipse at 50% 100%, rgba(0,0,0,0.55), transparent 60%),
      linear-gradient(180deg, var(--forest-mid) 0%, #4d8c2c 40%, #2c5a1c 75%, var(--forest-dark) 100%);
  }
  .hud-label {
    position: absolute; top: 24px;
    font-size: 22px; font-weight: 700; letter-spacing: 0.3px;
    text-shadow: 0 1px 3px rgba(0,0,0,0.5);
    transform: translateX(-50%);
  }
  .lives-label { left: 130px; }
  .level-label { left: 598px; }
  .moves-label { left: 1084px; }
  .lives-heart { position: absolute; left: 73px; top: 53px; width: 118px; height: 110px; }
  .lives-count {
    position: absolute; left: 73px; top: 62px; width: 118px; text-align: center;
    font-family: "Arimo", sans-serif; font-size: 54px; color: var(--heart-number);
    text-shadow: 0 0 2px #b00000;
  }
  .level-badge {
    position: absolute; left: 543px; top: 54px; width: 106px; height: 106px; border-radius: 50%;
    background: var(--level-fill); border: 2px solid var(--level-ring);
    display: flex; align-items: center; justify-content: center;
    font-size: 36px; font-weight: 700; box-shadow: 0 2px 6px rgba(0,0,0,0.35);
  }
  .moves-box {
    position: absolute; left: 1009px; top: 54px; width: 152px; height: 70px; border-radius: 6px;
    background: var(--moves-yellow); color: #000;
    display: flex; align-items: center; justify-content: center;
    font-size: 50px; font-weight: 800;
  }
  .puzzle-grid {
    position: absolute; left: 287px; top: 177px;
    display: grid; grid-template-columns: repeat(4, 140px); grid-template-rows: repeat(4, 130px);
    column-gap: 9px; row-gap: 7px;
  }
  .tile { border-radius: 7px; box-shadow: 0 2px 5px rgba(0,0,0,0.45), inset 0 0 0 2px rgba(0,0,0,0.08); }
  .tile-red { background: var(--tile-red); }
  .tile-yellow { background: var(--tile-yellow); }
  .tile-blue { background: var(--tile-blue); }
  .tile-green { background: var(--tile-green); }
  .progress-track {
    position: absolute; left: 102px; top: 782px; width: 918px; height: 44px;
    background: var(--bar-track); border: 1px solid rgba(255,255,255,0.35); border-radius: 5px; overflow: hidden;
  }
  .progress-fill {
    width: 50%; height: 100%;
    background: linear-gradient(180deg, var(--bar-fill-top), var(--bar-fill-bottom));
  }
  .progress-value {
    position: absolute; left: 0; top: 0; width: 100%; height: 100%;
    display: flex; align-items: center; justify-content: center;
    font-size: 21px; font-weight: 700; text-shadow: 0 1px 2px rgba(0,0,0,0.4);
  }
  .loading-text {
    position: absolute; left: 554px; top: 835px; transform: translateX(-50%);
    font-size: 22px; font-weight: 600;
  }
  .sound-toggle { position: absolute; left: 1050px; top: 782px; width: 72px; height: 46px; }
</style>
</head>
<body>
<main class="game-screen">
  <div class="forest-background" role="img" aria-label="Painted forest scene with tall trees and sunlit green foliage"></div>

  <div class="hud-label lives-label">LIVE</div>
  <svg class="lives-heart" viewBox="0 0 118 110" aria-hidden="true">
    <defs>
      <radialGradient id="heartShade" cx="40%" cy="30%" r="70%">
        <stop offset="0" stop-color="#ff6a6a"/>
        <stop offset="0.6" stop-color="#e8121e"/>
        <stop offset="1" stop-color="#a8000a"/>
      </radialGradient>
    </defs>
    <path d="M59 106 C40 88 4 66 4 34 C4 14 20 3 35 3 C46 3 55 9 59 19 C63 9 72 3 83 3 C98 3 114 14 114 34 C114 66 78 88 59 106 Z"
          fill="url(#heartShade)" stroke="#b80010" stroke-width="2"/>
    <ellipse cx="35" cy="24" rx="18" ry="9" fill="#fff" opacity="0.35"/>
  </svg>
  <div class="lives-count">13</div>

  <div class="hud-label level-label">LEVEL</div>
  <div class="level-badge">1</div>

  <div class="hud-label moves-label">MOVES</div>
  <div class="moves-box">3</div>

  <section class="puzzle-grid" aria-label="Puzzle board">
    <div class="tile tile-red"></div><div class="tile tile-yellow"></div><div class="tile tile-blue"></div><div class="tile tile-green"></div>
    <div class="tile tile-red"></div><div class="tile tile-yellow"></div><div class="tile tile-blue"></div><div class="tile tile-green"></div>
    <div class="tile tile-red"></div><div class="tile tile-yellow"></div><div class="tile tile-blue"></div><div class="tile tile-green"></div>
    <div class="tile tile-red"></div><div class="tile tile-yellow"></div><div class="tile tile-blue"></div><div class="tile tile-green"></div>
  </section>

  <div class="progress-track">
    <div class="progress-fill"></div>
    <div class="progress-value">50%</div>
  </div>
  <div class="loading-text">Loading...</div>

  <svg class="sound-toggle" viewBox="0 0 72 46" aria-label="Sound on">
    <path d="M4 15 H16 L32 3 V43 L16 31 H4 Z" fill="#fff"/>
    <path d="M40 15 Q46 23 40 31" fill="none" stroke="#fff" stroke-width="5" stroke-linecap="round"/>
    <path d="M49 8 Q60 23 49 38" fill="none" stroke="#fff" stroke-width="5" stroke-linecap="round"/>
  </svg>
</main>
</body>
</html>
```